The Harbourline Aid Trust needs a graphic of their innovation approach

What we need?
- we have designed a new innovation approach (see attached). An innovation approach is the process one goes through in order to design and launch a new product or service.
- This new graphic will be used in meetings to help others understand what innovation is and how we do it. It will also be used in training sessions and be the starting point for innovation training materials we are creating
- We have created this draft graphic by copying and pasting new words over another charities innovation process
- We would like you to use your design magic and create our very own innovation process graphic. We would like it to be neat, simple, non fussy, easy to understand /read and in line with our brand colours
Attached:
1. PowerPoint:
- Slide 1: our innovation process
- Slide 2 explanation of process to bring it to life
- Slide 3&4: brand colours
- Slide 5: inspiration / examples of other processes we like the look of
2. Typeface brand guidelines
We can't wait to see what you come up with! Thank you :)
internal employees
Charity

```html
<!DOCTYPE html>
<html lang="en">
<head>
<meta charset="utf-8">
<title>The Harbourline Aid Trust – Innovation Approach</title>
<link rel="stylesheet" href="https://fonts.googleapis.com/css2?family=Arimo:wght@400;700&display=swap">
<style>
  :root {
    --discover: #f0575a;
    --discover-title: #e21b22;
    --discover-soft: #f39a9a;
    --define: #f4b23c;
    --define-soft: #f8d293;
    --deliver: #1a8cbe;
    --deliver-soft: #8dc6df;
    --ink: #111111;
    --paper: #ffffff;
  }
  html, body {
    margin: 0;
    padding: 0;
    width: 1200px;
    height: 809px;
    overflow: hidden;
    background: var(--paper);
  }
  .innovation-approach {
    display: block;
    width: 1200px;
    height: 809px;
    font-family: "Arimo", Arial, sans-serif;
  }
  .phase-title { font-size: 22px; font-weight: 700; text-anchor: middle; }
  .phase-title--discover { fill: var(--discover-title); }
  .phase-title--define { fill: var(--define); }
  .phase-title--deliver { fill: var(--deliver); }

  .stage-ring { fill: var(--paper); stroke-width: 8; }
  .stage-ring--discover { stroke: var(--discover); }
  .stage-ring--define { stroke: var(--define); }
  .stage-ring--deliver { stroke: var(--deliver); }
  .stage-label { font-size: 14px; fill: var(--ink); text-anchor: middle; }

  .flow { fill: none; stroke-width: 8; }
  .flow--discover { stroke: var(--discover); }
  .flow--define { stroke: var(--define); }
  .flow--deliver { stroke: var(--deliver); }
  .head--discover { fill: var(--discover-title); }
  .head--define { fill: var(--define); }
  .head--deliver { fill: var(--deliver); }

  .loop { fill: none; stroke-width: 2; stroke-dasharray: 2 2.5; }
  .loop--discover { stroke: var(--discover-soft); }
  .loop--define { stroke: var(--define-soft); }
  .loop--deliver { stroke: var(--deliver-soft); }
  .loop-head--discover { fill: var(--discover-soft); }
  .loop-head--define { fill: var(--define-soft); }
  .loop-head--deliver { fill: var(--deliver-soft); }

  .step-label { font-size: 16px; text-anchor: middle; }
  .step-label--discover { fill: var(--discover-title); }
  .step-label--define { fill: var(--define); }
  .step-label--deliver { fill: var(--deliver); }
  .loop-label { font-size: 15px; text-anchor: middle; }
  .loop-label--discover { fill: var(--discover-soft); }
  .loop-label--define { fill: var(--define-soft); }
  .loop-label--deliver { fill: var(--deliver-soft); }
</style>
</head>
<body>
<svg class="innovation-approach" viewBox="0 0 850 573" role="img" aria-label="The Harbourline Aid Trust innovation approach: Discover, Define, Deliver">
  <g class="phase-titles">
    <text class="phase-title phase-title--discover" x="125" y="74">Discover</text>
    <text class="phase-title phase-title--define" x="452" y="74">Define</text>
    <text class="phase-title phase-title--deliver" x="722" y="74">Deliver</text>
  </g>

  <g class="iteration-loops">
    <path class="loop loop--discover" d="M200 160 H125 Q112 160 112 173 V236"/>
    <polygon class="loop-head--discover" points="108,236 116,236 112,244"/>
    <path class="loop loop--define" d="M412 240 V190"/>
    <path class="loop loop--discover" d="M412 190 V178 Q412 160 394 160 H325"/>
    <polygon class="loop-head--discover" points="325,156 325,164 317,160"/>
    <path class="loop loop--define" d="M522 480 H440 Q412 480 412 452 V381"/>
    <polygon class="loop-head--define" points="408,381 416,381 412,373"/>
    <path class="loop loop--deliver" d="M758 380 V462 Q758 480 740 480 H661"/>
    <polygon class="loop-head--deliver" points="661,476 661,484 653,480"/>
  </g>

  <g class="main-flow">
    <path class="flow flow--discover" d="M97 252 V176 Q97 148 125 148 H192"/>
    <polygon class="head--discover" points="191,137 206,148 191,159"/>
    <path class="flow flow--discover" d="M314 148 H397 Q410 148 418 155"/>
    <path class="flow flow--define" d="M417 154 Q424 162 424 178 V238"/>
    <polygon class="head--define" points="413,238 424,253 435,238"/>
    <path class="flow flow--define" d="M424 368 V440 Q424 468 452 468 H518"/>
    <polygon class="head--define" points="517,457 532,468 517,479"/>
    <path class="flow flow--deliver" d="M646 468 H717 Q745 468 745 440 V383"/>
    <polygon class="head--deliver" points="734,384 745,369 756,384"/>
    <path class="flow flow--deliver" d="M745 252 V185"/>
    <polygon class="head--deliver" points="734,186 745,170 756,186"/>
  </g>

  <g class="step-labels">
    <text class="step-label step-label--discover" x="145" y="130">Insight</text>
    <text class="loop-label loop-label--discover" x="155" y="188">Interate</text>
    <text class="step-label step-label--discover" x="362" y="131">Ideate</text>
    <text class="loop-label loop-label--discover" x="362" y="188">Interate</text>
    <text class="step-label step-label--define" x="498" y="215">(In)validate</text>
    <text class="step-label step-label--define" x="485" y="450">Test</text>
    <text class="loop-label loop-label--define" x="474" y="503">Interate</text>
    <text class="step-label step-label--deliver" x="689" y="434">Delivery</text>
    <text class="step-label step-label--deliver" x="689" y="455">Plan</text>
    <text class="loop-label loop-label--deliver" x="720" y="500">Continuous</text>
    <text class="loop-label loop-label--deliver" x="720" y="522">Improvement</text>
  </g>

  <g class="stages">
    <circle class="stage-ring stage-ring--discover" cx="97" cy="309" r="57"/>
    <text class="stage-label" x="97" y="314">Challenge</text>
    <circle class="stage-ring stage-ring--discover" cx="258" cy="148" r="57"/>
    <text class="stage-label" x="258" y="145">Opportunity</text>
    <text class="stage-label" x="258" y="163">Statement</text>
    <circle class="stage-ring stage-ring--define" cx="424" cy="311" r="57"/>
    <text class="stage-label" x="424" y="316">Concepts</text>
    <circle class="stage-ring stage-ring--deliver" cx="589" cy="473" r="57"/>
    <text class="stage-label" x="589" y="478">Solution</text>
    <circle class="stage-ring stage-ring--deliver" cx="745" cy="311" r="57"/>
    <text class="stage-label" x="745" y="316">Launch</text>
  </g>
</svg>
</body>
</html>
```